Photo Storage Service - Web Application

This is web design for a simple photo storage service.
There is a web page and on the left side is a list of folders and on the right side there are photo thumbnails. By pressing a photo thumbnail, they will see the full size (it's just a link to a different page).
This project is limited only to ONE page, which is the page with the folders list and the thumbnails. However it contains some features that I will try to list here:
- Name of the service: Teso Vault
- Location of account: http://username.tesovault.example
- Folder list: Show all folders belonging to the user. Because you have to be able to drag photos to a folder, they have to be visible and cannot be hidden behind a menu item etc.
- Thumbnails with photos (in the future also videos)
- Adjusted view with smaller thumbnails and less space for folder list (so it is possible to view a larger quantity of thumbnails)- Select multiple thumbnails with rectangle- Show that a thumbnail is selected (maybe bold border?)
- Simple mobile view, but no emphasis on the mobile view in this design project.
- Drag one or more selected photos to a folder
- Delete one or more selected photos
- Drag a folder to another folder
- Rename folder
- Delete folder
- Create folder
- Show progress when deleting/moving (because it calls for every photo, so if there are 100 photos, it will delete 1 by 1 and it will take about 10 seconds - you could show progress bar or equivalent)
Background information: This is for a photo storage service NOT intended for sharing photos, but intended to indefinitely store photos and for yourself to browse your own photos.
It is a design requirement that it loads extremely fast. So we need to limit as much as possible extra graphics that cannot be done by CSS and other external libraries.
(I know this is ONLY design and nothing to do with CSS or libraries, but I can assess from the design if it might be heavy to load when implemented)
I have attached a crude screenshot of the current design, just for your understanding. It should not match this design and you are not in any way supposed to FIT your design into this same style or structure.
Target Market(s)
Consumers
Number of Pages Required
1 page

```html
<!DOCTYPE html>
<html lang="en">
<head>
<meta charset="utf-8">
<title>Teso Vault – Photos</title>
<link href="https://fonts.googleapis.com/css2?family=Questrial&family=Montserrat:wght@600;700&family=Inter:wght@400&display=swap" rel="stylesheet">
<style>
:root{
  --ink:#222;
  --dark:#27282d;
  --dark-2:#333439;
  --accent:#ee3a48;
  --accent-light:#ff5e66;
  --rule:#d4d4d4;
  --row:#f7f7f7;
  --shadow:#d9d9d9;
  --white:#fff;
}
*{box-sizing:border-box;margin:0;padding:0}
html,body{width:1200px;height:903px;overflow:hidden;background:var(--white)}
body{position:relative;font-family:"Questrial",sans-serif;color:var(--ink)}
.topbar{position:absolute;left:0;top:0;width:1200px;height:84px;background:var(--dark)}
.brand{position:absolute;left:0;top:0;width:254px;height:84px;background:var(--white);padding:26px 0 0 47px}
.brand-name{font-size:27px;letter-spacing:1px;color:var(--dark);line-height:1}
.brand-url{font-size:6.5px;letter-spacing:1.6px;margin-top:4px;color:var(--dark)}
.accent-rule{position:absolute;left:0;top:84px;width:1200px;height:4px;background:var(--accent)}
.search{position:absolute;left:396px;top:21px;width:407px;height:44px;background:var(--white);border:3px solid var(--white)}
.search-scope{position:absolute;left:0;top:0;width:139px;height:38px;background:var(--dark);color:var(--white);font:400 13.5px "Inter",sans-serif;padding:11px 0 0 19px}
.search-scope svg{position:absolute;right:16px;top:16px}
.search-input{position:absolute;left:155px;top:12px;font:400 11.5px "Inter",sans-serif;color:#aaa}
.search-btn{position:absolute;right:0;top:0;width:38px;height:38px;background:var(--accent);display:flex;align-items:center;justify-content:center}
.account,.signout{position:absolute;top:34px;display:flex;align-items:center;gap:8px;color:var(--white);font:400 11px "Inter",sans-serif}
.account{left:949px}
.signout{left:1086px;gap:13px;top:33px}
.sortbar{position:absolute;left:0;top:88px;width:1200px;height:66px;background:radial-gradient(ellipse at center,var(--dark-2),var(--dark) 70%)}
.sort{position:absolute;top:15px;width:127px;height:36px;border:1px solid var(--white);border-radius:18px;color:var(--white);font:400 11.5px "Inter",sans-serif;display:flex;align-items:center;justify-content:center}
.folders{position:absolute;left:0;top:154px;width:254px}
.folder{height:61.6px;border-bottom:1px solid #c8c8c8;border-right:1px solid #c8c8c8;background:linear-gradient(#fff,var(--row));display:flex;align-items:center;justify-content:space-between;padding:0 15px 0 17px;font-size:19px}
.folder svg{flex:none}
.folder.create{background:linear-gradient(90deg,var(--accent),var(--accent-light) 55%,var(--accent));color:#1f1f1f;font:700 18px/1.1 "Montserrat",sans-serif;border:0}
.grid{position:absolute;left:268px;top:171px;width:914px}
.card{position:absolute;width:282px;text-align:center}
.thumb-wrap{position:relative;width:282px;height:192px}
.thumb-wrap::before{content:"";position:absolute;left:13px;top:14px;width:269px;height:178px;background:var(--shadow)}
.thumb{position:absolute;left:0;top:0;width:269px;height:178px;border:1px solid #bbb}
.card h3{margin-top:11px;font:600 13.5px "Montserrat",sans-serif;letter-spacing:.2px;width:269px}
.card p{width:269px;margin-top:5px;font-size:11.4px;line-height:13.4px;color:#444}
.divider{position:absolute;left:268px;top:469px;width:914px;height:1px;background:#e6e6e6}
.pager{position:absolute;top:820px;left:0;width:1200px}
.pager a{position:absolute;top:0;height:37px;width:37px;display:flex;align-items:center;justify-content:center;font:700 18px "Montserrat",sans-serif;color:var(--ink);text-decoration:none}
.pager a.current{background:var(--accent);color:var(--white)}
.footer-rule{position:absolute;left:0;top:897px;width:1200px;height:6px;background:var(--dark)}
</style>
</head>
<body>
<header class="topbar">
  <div class="brand">
    <div class="brand-name">TESO VAULT</div>
    <div class="brand-url">HTTP://USERNAME.TESOVAULT.EXAMPLE</div>
  </div>
  <form class="search">
    <div class="search-scope">SEARCH FOR
      <svg width="9" height="6" viewBox="0 0 9 6"><path d="M0 0h9L4.5 6z" fill="#fff"/></svg></div>
    <span class="search-input">What are you searching for...</span>
    <div class="search-btn"><svg width="20" height="20" viewBox="0 0 20 20" fill="none" stroke="#fff" stroke-width="2.4"><circle cx="8.5" cy="8.5" r="6"/><path d="M13 13l5 5"/></svg></div>
  </form>
  <div class="account"><svg width="18" height="20" viewBox="0 0 18 20" fill="none" stroke="#fff" stroke-width="1.3"><circle cx="9" cy="6" r="4.5"/><path d="M1 19c0-5 3.5-7.5 8-7.5s8 2.5 8 7.5z"/></svg>MY ACCOUNT</div>
  <div class="signout"><svg width="31" height="28" viewBox="0 0 31 28"><rect x="1.5" y="1.5" width="17" height="25" fill="none" stroke="#fff" stroke-width="3"/><rect x="7" y="4" width="24" height="20" fill="var(--accent)"/><path d="M12 14h11M18 9l5 5-5 5" fill="none" stroke="#222" stroke-width="2.4"/></svg>SIGN OUT</div>
</header>
<div class="accent-rule"></div>

<nav class="sortbar">
  <div class="sort" style="left:368px">Sort by Cartegories</div>
  <div class="sort" style="left:537px">Sort by Date</div>
  <div class="sort" style="left:705px">Sort by Name</div>
</nav>

<svg width="0" height="0" style="position:absolute">
  <defs>
    <g id="gear"><circle cx="17" cy="17" r="17" fill="#222"/><g fill="#fff" transform="translate(17 17)"><circle r="6.5"/><rect x="-2.3" y="-10" width="4.6" height="20"/><rect x="-2.3" y="-10" width="4.6" height="20" transform="rotate(45)"/><rect x="-2.3" y="-10" width="4.6" height="20" transform="rotate(90)"/><rect x="-2.3" y="-10" width="4.6" height="20" transform="rotate(135)"/></g><circle cx="17" cy="17" r="3" fill="#222"/></g>
  </defs>
</svg>

<aside class="folders">
  <div class="folder">INBOX<svg width="34" height="34"><use href="#gear"/></svg></div>
  <div class="folder">80’S PARTY<svg width="34" height="34"><use href="#gear"/></svg></div>
  <div class="folder">A TOUR IN OSLO<svg width="34" height="34"><use href="#gear"/></svg></div>
  <div class="folder">THAILAND 1<svg width="34" height="34"><use href="#gear"/></svg></div>
  <div class="folder">THAILAND 2<svg width="34" height="34"><use href="#gear"/></svg></div>
  <div class="folder">TIMELINE PHOTOS<svg width="34" height="34"><use href="#gear"/></svg></div>
  <div class="folder">RANDOM<svg width="34" height="34"><use href="#gear"/></svg></div>
  <div class="folder">BRAZIL<svg width="34" height="34"><use href="#gear"/></svg></div>
  <div class="folder">TEA GARDEN<svg width="34" height="34"><use href="#gear"/></svg></div>
  <div class="folder create"><span>CREATE<br>NEW FOLDER</span><svg width="34" height="34" viewBox="0 0 34 34"><circle cx="17" cy="17" r="17" fill="#222"/><path d="M17 8v18M8 17h18" stroke="var(--accent)" stroke-width="5"/></svg></div>
</aside>

<main>
  <div class="card" style="left:272px;top:171px">
    <div class="thumb-wrap"><div class="thumb" role="img" aria-label="Mountain ridge at sunset" style="background:linear-gradient(160deg,#d9b97a,#8a8a52 45%,#4d5a2c)"></div></div>
    <h3>IMAGE TITLE</h3><p>Lorem ipsum dolor sit amet, consectetur adipisc-ing elit, sed do eiusmod tempor incididunt ut labore et dolore magna aliqua</p>
  </div>
  <div class="card" style="left:585px;top:171px">
    <div class="thumb-wrap"><div class="thumb" role="img" aria-label="Fjord seen from a cliff edge" style="background:linear-gradient(120deg,#2d4a4f,#5f8c86 50%,#c9dfd6)"></div></div>
    <h3>IMAGE TITLE</h3><p>Lorem ipsum dolor sit amet, consectetur adipisc-ing elit, sed do eiusmod tempor incididunt ut labore et dolore magna aliqua</p>
  </div>
  <div class="card" style="left:899px;top:171px">
    <div class="thumb-wrap"><div class="thumb" role="img" aria-label="Autumn trees reflected in a mountain lake" style="background:linear-gradient(180deg,#a8c4dc,#c1733a 45%,#6e8fa8)"></div></div>
    <h3>IMAGE TITLE</h3><p>Lorem ipsum dolor sit amet, consectetur adipisc-ing elit, sed do eiusmod tempor incididunt ut labore et dolore magna aliqua</p>
  </div>
  <div class="divider"></div>
  <div class="card" style="left:272px;top:507px">
    <div class="thumb-wrap"><div class="thumb" role="img" aria-label="City skyline lit at night from above" style="background:linear-gradient(160deg,#1f2550,#3a3360 40%,#8a6a3a)"></div></div>
    <h3>IMAGE TITLE</h3><p>Lorem ipsum dolor sit amet, consectetur adipisc-ing elit, sed do eiusmod tempor incididunt ut labore et dolore magna aliqua</p>
  </div>
  <div class="card" style="left:585px;top:507px">
    <div class="thumb-wrap"><div class="thumb" role="img" aria-label="Hanging vines over green water" style="background:linear-gradient(150deg,#5a7a3a,#1f6e62 45%,#14483f)"></div></div>
    <h3>IMAGE TITLE</h3><p>Lorem ipsum dolor sit amet, consectetur adipisc-ing elit, sed do eiusmod tempor incididunt ut labore et dolore magna aliqua</p>
  </div>
  <div class="card" style="left:899px;top:507px">
    <div class="thumb-wrap"><div class="thumb" role="img" aria-label="Red brick gothic building with clock tower" style="background:linear-gradient(180deg,#4f7fb0,#9aaabb 30%,#8a3a2a 60%,#5a2a22)"></div></div>
    <h3>IMAGE TITLE</h3><p>Lorem ipsum dolor sit amet, consectetur adipisc-ing elit, sed do eiusmod tempor incididunt ut labore et dolore magna aliqua</p>
  </div>
</main>

<nav class="pager">
  <a style="left:566px" aria-label="Previous"><svg width="28" height="24" viewBox="0 0 28 24" fill="none" stroke="var(--accent)" stroke-width="4.5"><path d="M13 2L3 12l10 10M25 2L15 12l10 10"/></svg></a>
  <a class="current" style="left:632px">1</a>
  <a style="left:684px">2</a>
  <a style="left:738px">3</a>
  <a style="left:791px">4</a>
  <a style="left:842px" aria-label="Next"><svg width="28" height="24" viewBox="0 0 28 24" fill="none" stroke="var(--accent)" stroke-width="4.5"><path d="M3 2l10 10L3 22M15 2l10 10-10 10"/></svg></a>
</nav>
<div class="footer-rule"></div>
</body>
</html>
```